A-Frame Sign for CPR Training

Summit Readiness Academy provides CPR and First Aid classes to businesses and individuals throughout Northern California. We are in need of a 36in TALL x 24in WIDE poster insert to use on our A-Frame sign. We need the design to include:

1. our logo (see attachment)
2. a border (professional and clean, but catchy)
3. our contact information including phone #: 916-784-3126 and website: www.BlueRiverSkills.example
4. basic product info and price, possibly include a small picture for each?
"CPR - $39" and "BLS" - $49"
5. the phases: "CPR and First Aid Classes" and "Taught by Firefighters" and "Sacramento | Stockton | Modesto"
6. use our theme colors of blue(003399) and green(80cc33)
7. EXTRA CREDIT: somewhere place a small "camera" icon with the words "snap a picture of me for later"

Industry/Entity Type

Training

Font styles to use
Serif

Requirements
Nice to have
• EXTRA CREDIT: somewhere place a small "camera" icon with the words "snap a picture of me for later"

```html
<!DOCTYPE html>
<html lang="en">
<head>
<meta charset="utf-8">
<title>Summit Readiness Academy – A-Frame Sign</title>
<link href="https://fonts.googleapis.com/css2?family=Lato:wght@400&family=Libre+Baskerville:wght@400&display=swap" rel="stylesheet">
<style>
  :root {
    --brand-blue: #24409a;
    --brand-green: #7ec242;
    --paper: #ffffff;
    --photo-warm: #6b5a48;
    --photo-dark: #3a3631;
    --photo-grey: #8a8782;
    --photo-shadow: #4d4a46;
  }
  html, body {
    margin: 0;
    padding: 0;
    overflow: hidden;
    background: var(--paper);
  }
  .sign {
    position: relative;
    width: 801px;
    height: 1200px;
    overflow: hidden;
    font-family: "Lato", Arial, sans-serif;
    color: var(--brand-blue);
    background: var(--brand-green);
  }
  .sign__frame {
    position: absolute;
    inset: 0;
  }
  .centered {
    position: absolute;
    left: 0;
    width: 801px;
    text-align: center;
    margin: 0;
    line-height: 1;
    font-weight: 400;
  }
  .brand-name {
    top: 118px;
    font-family: "Libre Baskerville", Georgia, serif;
    font-size: 27px;
    letter-spacing: 1px;
    color: var(--brand-blue);
  }
  .headline {
    top: 224px;
    font-size: 35px;
    letter-spacing: 2.5px;
  }
  .locations {
    top: 285px;
    font-size: 25px;
    letter-spacing: 2px;
  }
  .price-tag {
    position: absolute;
    top: 370px;
    height: 56px;
    width: 265px;
    border-radius: 14px;
    background: var(--brand-green);
    color: var(--paper);
    font-size: 33px;
    letter-spacing: 4px;
    line-height: 56px;
    text-align: center;
  }
  .price-tag--cpr { left: 97px; }
  .price-tag--bls { left: 440px; }
  .course-photo {
    position: absolute;
    top: 460px;
    width: 305px;
    height: 254px;
    border: 6px solid var(--brand-green);
    border-radius: 22px;
  }
  .course-photo--cpr {
    left: 68px;
    background: linear-gradient(160deg, var(--photo-warm) 0%, var(--photo-dark) 45%, var(--photo-grey) 100%);
  }
  .course-photo--bls {
    left: 414px;
    background: linear-gradient(200deg, var(--photo-grey) 0%, var(--photo-shadow) 60%, var(--photo-grey) 100%);
  }
  .schedule {
    top: 783px;
    font-size: 50px;
    letter-spacing: 8px;
  }
  .instructors {
    top: 857px;
    font-size: 32px;
    letter-spacing: 5px;
  }
  .divider {
    position: absolute;
    left: 63px;
    width: 675px;
    height: 2px;
    background: var(--brand-green);
  }
  .divider--top { top: 943px; }
  .divider--bottom { top: 1067px; }
  .contact {
    position: absolute;
    left: 0;
    width: 801px;
    display: flex;
    justify-content: center;
    align-items: center;
    gap: 12px;
    font-size: 33px;
  }
  .contact--phone { top: 952px; height: 50px; }
  .contact--web { top: 1015px; height: 46px; }
  .contact__icon { display: block; }
  .snap-note {
    position: absolute;
    top: 1102px;
    left: 0;
    width: 801px;
    display: flex;
    justify-content: center;
    align-items: center;
    gap: 18px;
    font-size: 15px;
    letter-spacing: 3px;
  }
</style>
</head>
<body>
<div class="sign">
  <svg class="sign__frame" width="801" height="1200" viewBox="0 0 801 1200" aria-hidden="true">
    <path d="M 45,6 Q 400,88 756,6 Q 830,600 756,1194 Q 400,1112 45,1194 Q -28,600 45,6 Z" fill="#ffffff"/>
  </svg>

  <p class="centered brand-name">SUMMIT READINESS ACADEMY, INC.</p>

  <h1 class="centered headline">CPR AND FIRST AID CLASSES</h1>
  <p class="centered locations">SACRAMENTO | STOCKTON | MODESTO</p>

  <div class="price-tag price-tag--cpr">CPR - $39</div>
  <div class="price-tag price-tag--bls">BLS - $49</div>

  <div class="course-photo course-photo--cpr" role="img" aria-label="Photo of a bystander giving CPR to a person lying on a street at night while another calls for help"></div>
  <div class="course-photo course-photo--bls" role="img" aria-label="Overhead photo of rescuers using an AED on a patient lying on a concrete floor"></div>

  <h2 class="centered schedule">WEEKLY CLASSES</h2>
  <p class="centered instructors">TAUGHT BY FIREFIGHTERS</p>

  <div class="divider divider--top"></div>

  <div class="contact contact--phone">
    <svg class="contact__icon" width="26" height="46" viewBox="0 0 26 46" aria-hidden="true">
      <rect x="7" y="0" width="3" height="8" fill="var(--brand-green)"/>
      <rect x="1" y="7" width="24" height="38" rx="4" fill="var(--brand-green)"/>
      <rect x="5" y="11" width="16" height="11" fill="#ffffff"/>
      <g fill="#ffffff">
        <rect x="5" y="26" width="4" height="3"/><rect x="11" y="26" width="4" height="3"/><rect x="17" y="26" width="4" height="3"/>
        <rect x="5" y="31" width="4" height="3"/><rect x="11" y="31" width="4" height="3"/><rect x="17" y="31" width="4" height="3"/>
        <rect x="5" y="36" width="4" height="3"/><rect x="11" y="36" width="4" height="3"/><rect x="17" y="36" width="4" height="3"/>
      </g>
    </svg>
    <span>916-784-3126</span>
  </div>

  <div class="contact contact--web">
    <svg class="contact__icon" width="42" height="42" viewBox="0 0 42 42" aria-hidden="true">
      <circle cx="21" cy="21" r="20" fill="var(--brand-green)"/>
      <g fill="none" stroke="#ffffff" stroke-width="2">
        <circle cx="21" cy="21" r="13"/>
        <ellipse cx="21" cy="21" rx="6" ry="13"/>
        <line x1="8" y1="21" x2="34" y2="21"/>
        <line x1="21" y1="8" x2="21" y2="34"/>
        <path d="M 10,14 Q 21,18 32,14"/>
        <path d="M 10,28 Q 21,24 32,28"/>
      </g>
    </svg>
    <span>www.BlueRiverSkills.example</span>
  </div>

  <div class="divider divider--bottom"></div>

  <div class="snap-note">
    <svg width="32" height="26" viewBox="0 0 32 26" aria-hidden="true">
      <rect x="9" y="1" width="12" height="6" rx="2" fill="var(--brand-green)"/>
      <rect x="0" y="4" width="32" height="22" rx="5" fill="var(--brand-green)"/>
      <circle cx="16" cy="15" r="6.5" fill="#ffffff"/>
      <circle cx="16" cy="15" r="4" fill="var(--brand-green)"/>
    </svg>
    <span>SNAP A PICTURE OF ME FOR LATER</span>
  </div>
</div>
</body>
</html>
```